Kelverin Roofing & Restoration Business Card Design

Lookiing for a double sided business card design that will have rounded corners, will look good with Spot UV, Soft Laminate, or Gloss
Front of card should have Logo, Name and Contact Info, License numbers
Back of card should have Logo, maybe other small details

```html
<!DOCTYPE html>
<html lang="en">
<head>
<meta charset="utf-8">
<title>Kelverin Roofing &amp; Restoration – Business Card</title>
<link href="https://fonts.googleapis.com/css2?family=Montserrat:wght@500;600;700&display=swap" rel="stylesheet">
<style>
  :root {
    --page: #1c1c1f;
    --card-dark: #141416;
    --card-mid: #2a2a2d;
    --card-light: #4a4a4d;
    --accent: #1b9ad6;
    --text: #f2f2f2;
    --text-soft: #e4e4e4;
    --silver: #d9d9d9;
  }
  * { box-sizing: border-box; margin: 0; padding: 0; }
  html, body { width: 1200px; height: 948px; overflow: hidden; background: var(--page); }
  body {
    font-family: "Montserrat", sans-serif;
    position: relative;
  }
  .card {
    position: absolute;
    left: 250px;
    width: 700px;
    height: 400px;
    border-radius: 26px;
    overflow: hidden;
    border-bottom: 5px solid var(--accent);
    box-shadow: 0 14px 30px rgba(0,0,0,.55);
  }
  .card--back { top: 40px; background: var(--card-dark); }
  .card--front {
    top: 508px;
    background: linear-gradient(120deg, var(--card-light) 0%, var(--card-mid) 30%, var(--card-dark) 60%, #111113 100%);
  }

  /* back */
  .back-pattern {
    position: absolute; inset: 0;
    background: linear-gradient(115deg, #f0f0f0 0%, #9a9a9a 22%, #4d4d50 42%, #1d1d20 62%, #0c0c0e 100%);
    opacity: .9;
  }
  .back-name {
    position: absolute; left: 0; right: 0; top: 50%;
    transform: translateY(-50%);
    text-align: center;
    font-weight: 700; font-size: 34px; letter-spacing: 2px;
    color: var(--text);
  }

  /* front */
  .brand {
    position: absolute; left: 48px; bottom: 70px;
    display: flex; align-items: center; gap: 14px;
  }
  .brand-mark {
    width: 14px; height: 14px; border-radius: 50%; background: var(--accent);
  }
  .brand-name {
    font-weight: 700; font-size: 22px; line-height: 1.2; letter-spacing: 1px;
    color: var(--text); text-transform: uppercase;
  }
  .divider {
    position: absolute; left: 372px; top: 60px; width: 2px; height: 280px;
    background: var(--accent);
  }
  .contact { position: absolute; left: 398px; top: 52px; color: var(--text-soft); }
  .contact-name { font-weight: 700; font-size: 30px; color: var(--accent); line-height: 1.1; }
  .contact-title { font-weight: 500; font-size: 15px; margin: 6px 0 14px; }
  .contact-line { font-weight: 500; font-size: 15px; line-height: 1.55; }
  .contact-list { list-style: none; margin-top: 10px; }
  .contact-list li {
    display: flex; align-items: center; gap: 10px;
    font-weight: 500; font-size: 15px; line-height: 1.7;
  }
  .contact-list svg { width: 15px; height: 15px; fill: var(--accent); flex: none; }
</style>
</head>
<body>

<section class="card card--back" aria-label="Card back">
  <div class="back-pattern" role="img" aria-label="Repeating brand mark pattern in spot UV, fading from silver to black"></div>
  <div class="back-name">KELVERIN</div>
</section>

<section class="card card--front" aria-label="Card front">
  <div class="brand">
    <span class="brand-mark"></span>
    <div class="brand-name">Kelverin<br>Roofing &amp;<br>Restoration</div>
  </div>

  <div class="divider"></div>

  <div class="contact">
    <div class="contact-name">Daniel Hartwell</div>
    <div class="contact-title">Managing Director</div>
    <div class="contact-line">Your address, City</div>
    <div class="contact-line">State, Zip 1234</div>
    <div class="contact-line">License #1234590</div>
    <ul class="contact-list">
      <li>
        <svg viewBox="0 0 24 24" aria-hidden="true"><path d="M6.6 10.8a15.1 15.1 0 0 0 6.6 6.6l2.2-2.2c.3-.3.7-.4 1-.2 1.1.4 2.3.6 3.6.6.6 0 1 .4 1 1V20c0 .6-.4 1-1 1A17 17 0 0 1 3 4c0-.6.4-1 1-1h3.5c.6 0 1 .4 1 1 0 1.3.2 2.5.6 3.6.1.3 0 .7-.2 1z"/></svg>
        123 456 789
      </li>
      <li>
        <svg viewBox="0 0 24 24" aria-hidden="true"><path d="M2 5h20v14H2zM4 7v.4l8 5 8-5V7z"/></svg>
        info@yourgmail.com
      </li>
      <li>
        <svg viewBox="0 0 24 24" aria-hidden="true"><circle cx="12" cy="12" r="10"/></svg>
        www.yourwebsite.com
      </li>
    </ul>
  </div>
</section>

</body>
</html>
```